Solvane Vitality MediSpa Brochure

We need a new brochure design. The old is attached.

We are wanting a three panel brochure for med spa designed and ready for print. The brochure will have content and images on both sides. We attached the old brochure in pdf format. The content needs to stay as on the attached pdf but please feel free to offer new designs. The color needs to match the attached logo, which is a light blue and teal. All images we want on the brochure are also attached.

The design must have an 1/8 in space from each edge for printing purposes

Target Market(s)

Men and Women

Industry/Entity Type

Wellness

Font styles to use
Sans Serif

Colors
34a6d7
33b8a4

Requirements
Must have
• soft curves. must have a 1/8 in space on all edges (including interior) to give bleed space for printing. Use content written on attached brochure.

```html
<!DOCTYPE html>
<html lang="en">
<head>
<meta charset="utf-8">
<title>Solvane Vitality MediSpa Brochure</title>
<link href="https://fonts.googleapis.com/css2?family=Open+Sans:wght@400;600;700&family=Lora:ital@1&display=swap" rel="stylesheet">
<style>
  :root{
    --blue:#34a6d7;
    --blue-deep:#2a9bd3;
    --teal:#33b8a4;
    --teal-deep:#1f8e7d;
    --ink:#3b3b3b;
    --mist:#eef0f2;
    --white:#ffffff;
  }
  *{box-sizing:border-box;margin:0;padding:0}
  html,body{width:1200px;height:927px;overflow:hidden;background:var(--white)}
  body{font-family:"Open Sans",Arial,sans-serif;color:var(--ink);position:relative}
  .hero{position:absolute;left:0;top:0;width:803px;height:341px;
    background:linear-gradient(180deg,#bfe0f5 0%,#e6f2fb 45%,#f4efe6 70%,#d9a07a 85%,#c0553f 100%)}
  .about-band{position:absolute;left:0;top:345px;width:398px;height:52px;background:var(--blue-deep);border-top-right-radius:26px}
  .script{font-family:"Lora",Georgia,serif;font-style:italic;font-weight:400;color:var(--white)}
  .about-band h2{font-size:36px;line-height:52px;padding-left:34px}
  .profile-bg{position:absolute;left:0;top:397px;width:400px;height:200px;background:var(--mist);border-bottom-right-radius:30px}
  .portrait{position:absolute;left:12px;top:405px;width:212px;height:178px;
    background:linear-gradient(160deg,#7fa55c 0%,#4f7a3c 55%,#3c5a2c 100%);border-radius:10px}
  .doctor{position:absolute;left:232px;top:580px}
  .doctor .name{color:var(--blue);font-weight:700;font-size:16px;line-height:20px}
  .doctor .cred{font-size:14px;line-height:18px;color:var(--ink)}
  .quotes{position:absolute;left:18px;top:632px;width:372px;font-size:14px;line-height:19.5px}
  .quotes p{margin-bottom:11px}
  .services{position:absolute;left:402px;top:0;width:355px}
  .services h3{position:absolute;left:18px;color:var(--blue);font-weight:400;font-size:21px;width:340px;
    border-bottom:2px solid var(--blue);padding-bottom:3px;line-height:26px}
  .services ul{position:absolute;list-style:none;font-size:15px;line-height:23.5px}
  .services li::before{content:"";display:inline-block;width:6px;height:6px;border-radius:50%;background:var(--teal);margin-right:10px;vertical-align:middle}
  .services .sub{padding-left:28px}
  .services .sub::before{background:var(--blue)}
  .laser{position:absolute;left:803px;top:0;width:397px;height:905px;background:var(--teal)}
  .laser-head{height:73px;background:var(--teal-deep);border-bottom-left-radius:26px}
  .laser-head h2{font-size:38px;line-height:73px;padding-left:16px}
  .treatment{position:absolute;left:12px;width:375px;color:var(--white)}
  .treatment h3{font-weight:400;font-size:21px;line-height:28px;border-bottom:2px solid var(--white);padding-bottom:2px;margin-bottom:6px}
  .treatment p{font-size:13.5px;line-height:19.5px}
  .foot{position:absolute;left:0;top:905px;width:1200px;height:22px;background:var(--teal)}
</style>
</head>
<body>
  <div class="hero" role="img" aria-label="Photo of a smiling woman in a white sun hat in a flower meadow under a blue sky"></div>

  <div class="profile-bg"></div>
  <div class="about-band"><h2 class="script">About Us</h2></div>
  <div class="portrait" role="img" aria-label="Portrait photo of Dr. Elena Marsh outdoors"></div>
  <div class="doctor">
    <div class="name">Dr.Elena Marsh,</div>
    <div class="cred">MD Facs</div>
  </div>
  <div class="quotes">
    <p>“Rejuvenation and reconstruction of the face are my passion, whether it is to improve one’s visual functions or to enhance one’s appearance.”</p>
    <p>“I personally perform all of my injections and CO2 laser treatments because safety and satisfaction are my top priorities.”</p>
    <p>“I was called by God to become a physician at the age of seven years old. I am motivated by a desire to serve others by providing superb medical care. I constantly strive to do my best.”</p>
  </div>

  <section class="services">
    <h3 style="top:340px">Injectables</h3>
    <ul style="left:28px;top:380px">
      <li>Neurelax</li><li>Chinora</li><li>Relaxa</li><li>Dermafill</li><li>Restora</li>
    </ul>
    <ul style="left:233px;top:380px">
      <li>PRP</li><li>Velura</li><li>Volara</li><li>Contoura</li>
    </ul>
    <h3 style="top:512px">Facials &amp; Chemical Peels</h3>
    <ul style="left:28px;top:560px;line-height:24px">
      <li>Microneedling with PRP</li><li>Dermaplane Facial</li><li>Medical Grade Chemical Peel</li><li>Facials</li><li>Waxing</li><li>AquaGlow MD</li>
    </ul>
    <h3 style="top:706px">Wellness Treatments</h3>
    <ul style="left:28px;top:748px;line-height:24.5px">
      <li>B-12 Injections</li>
      <li class="sub">Lipo B - Weight Loss</li>
      <li class="sub">Lipo B + Carnitine - Muscle Builsing</li>
      <li>Hormone Replacement Therapy</li>
    </ul>
    <h3 style="top:866px">Skincare &amp; Lumiderm</h3>
  </section>

  <aside class="laser">
    <div class="laser-head"><h2 class="script">Laser Treatments</h2></div>
    <div class="treatment" style="top:88px">
      <h3>Laser Hair Removal</h3>
      <p>Laser hair removal is a great solution for those who no longer want to continue shaving, tweezing or waxing to remove unwanted hair. Our innovative laser hair removal treatments can permanently remove unwnted body hair.</p>
    </div>
    <div class="treatment" style="top:246px">
      <h3>Femina Renew</h3>
      <p>Femina Renew is an outpatient, minimally invasive, non-hormonal vaginal procedure designed to stimulate new collagen production for healthier tissue. This proced;ure treats dryness, itchiness, loss of sinsation and stress incontinece.</p>
    </div>
    <div class="treatment" style="top:409px">
      <h3>CO2 Resurfacing</h3>
      <p>The CO2 Laser is the highest power continuous laser, making it ideal for resurfacing. The wavelengths produced are ideal the energy to be absorbed in the skin and produce excellent results. It reduces wrinkles. age spots, and stimulates collagen production.</p>
    </div>
    <div class="treatment" style="top:598px">
      <h3>IPL Photofacial</h3>
      <p>Brown spots, broken capillaries and other fallout from photo aging are easy targets for this laser system, which uses broadband light to repair these defects.</p>
    </div>
    <div class="treatment" style="top:746px">
      <h3>IPL Achne/Rosacea/Spider Vein</h3>
      <p>Achne can be treated nonablatively using IPL, a relatively low-energy, short pulse of broadband light, resulting in an improvement of the skin’s appearance with less breakouts. Rosacea and spider veins are also reduced using IPL.</p>
    </div>
  </aside>

  <div class="foot"></div>
</body>
</html>
```